Print materials for 3-star hotel

We are changing up our print materials (notepads, letterheads, key card jackets, small flyer for the room rates) We are a 3 star business hotel in the Philippines and have mainly used grey tones and clean, simple lines. See attached photos for logo and hotel interior photos.

Target Market(s)

Business

Contact Information for Business Card

Corvina Terrace Hotel
Magistrate Lunod Avenue corner Pabilo St Cebu City 6000 Philippines
Tel: +63 32 481 7520
Mobile: +63 917 604 2893
www.corvinaterracehotel.example

Font styles to use
Serif
Sans Serif

Requirements
Must have
• Simple
• Readable font and font size
Nice to have
• Neutral colors, grey and taupes
Should not have
• No purples and bright blues

```html
<!DOCTYPE html>
<html lang="en">
<head>
<meta charset="utf-8">
<title>Corvina Terrace Hotel — Stationery</title>
<link rel="stylesheet" href="https://fonts.googleapis.com/css2?family=Cormorant+Garamond:wght@500&family=Roboto+Condensed:wght@300&display=swap">
<style>
  :root {
    --canvas: #e9eaec;
    --paper: #ffffff;
    --ink: #1c1c1c;
    --ink-soft: #5a5a5a;
    --rule: #8c8c8c;
    --silver: #c9c9cb;
    --speckle: #dcdde0;
    --ghost: #eeeff1;
  }
  * { box-sizing: border-box; margin: 0; padding: 0; }
  html, body { width: 894px; height: 1200px; overflow: hidden; }
  body { background: var(--canvas); position: relative; font-family: "Roboto Condensed", Arial, sans-serif; color: var(--ink-soft); }

  .sheet { position: absolute; background: var(--paper); box-shadow: 0 1px 4px rgba(0,0,0,.18); overflow: hidden; }
  .texture { position: absolute; left: 0; right: 0; }
  .texture--fade { background: linear-gradient(to bottom, rgba(220,221,224,0), var(--speckle) 55%, rgba(220,221,224,.4)); }

  .brand { position: absolute; left: 0; right: 0; text-align: center; font-family: "Cormorant Garamond", Georgia, serif; font-weight: 500; color: var(--ink); }
  .brand__mark { display: block; margin: 0 auto 6px; background: var(--ink); }
  .brand__name { display: block; letter-spacing: .2em; white-space: nowrap; }
  .brand__sub { display: block; letter-spacing: .3em; }

  .ghost-square { position: absolute; background: var(--ghost); }

  .small { font-size: 5.6px; line-height: 1.5; color: var(--ink-soft); }

  /* notepad */
  .notepad { left: 35px; top: 348px; width: 206px; height: 267px; }
  .notepad__frame { position: absolute; inset: 9px; border: 1.4px solid var(--rule); }
  .notepad .texture { top: 120px; bottom: 0; }
  .notepad__url { position: absolute; left: 0; right: 0; bottom: 24px; text-align: center; }

  /* business cards */
  .card { left: 258px; width: 215px; height: 124px; }
  .card--front { top: 348px; border: 5px solid var(--silver); }
  .card--back { top: 491px; }
  .card--back .card__frame { position: absolute; inset: 9px; border: 1.2px solid var(--silver); }
  .card__rule { position: absolute; left: 33px; right: 33px; top: 76px; border-top: 1px solid var(--rule); }
  .card__cols { position: absolute; top: 82px; left: 0; right: 0; display: flex; justify-content: center; gap: 10px; }
  .card__cols .left { text-align: right; }

  /* envelope */
  .envelope { left: 35px; top: 669px; width: 443px; height: 221px; }
  .envelope .texture { top: 40px; bottom: 0; background: linear-gradient(160deg, rgba(220,221,224,0) 20%, var(--speckle) 60%, rgba(220,221,224,.5)); }
  .envelope__contact { position: absolute; left: 28px; top: 178px; }
  .envelope__rule { position: absolute; right: 0; width: 230px; top: 205px; border-top: 1px solid var(--rule); }

  /* letterhead */
  .letterhead { left: 495px; top: 348px; width: 354px; height: 502px; }
  .letterhead .texture { top: 360px; bottom: 0; background: linear-gradient(to bottom, rgba(220,221,224,0), rgba(220,221,224,.7)); }
  .letterhead__foot { position: absolute; left: 0; right: 0; top: 461px; display: flex; align-items: center; gap: 6px; padding: 0 0; }
  .letterhead__foot .line { flex: 1; border-top: 1px solid var(--rule); }
  .letterhead__foot .text { text-align: center; }
</style>
</head>
<body>

  <!-- notepad -->
  <section class="sheet notepad">
    <div class="texture texture--fade" role="img" aria-label="Soft silver speckle texture"></div>
    <div class="notepad__frame"></div>
    <div class="brand" style="top:26px">
      <span class="brand__mark" style="width:18px;height:18px"></span>
      <span class="brand__name" style="font-size:11px">CORVINA TERRACE</span>
      <span class="brand__sub" style="font-size:7px">HOTEL</span>
    </div>
    <p class="small notepad__url">www.corvinaterracehotel.example</p>
  </section>

  <!-- business card front -->
  <section class="sheet card card--front">
    <div class="brand" style="top:14px">
      <span class="brand__mark" style="width:17px;height:17px;margin-bottom:4px"></span>
      <span class="brand__name" style="font-size:10px">CORVINA TERRACE</span>
      <span class="brand__sub" style="font-size:6.5px">HOTEL</span>
    </div>
    <div class="card__rule"></div>
    <div class="card__cols small">
      <p class="left">+63 32 481 7520 &nbsp;|&nbsp; +63 32 481 7534<br>reservations@corvinaterracehotel.example<br>www.corvinaterracehotel.example</p>
      <p>Magistrate Lunod Avenue corner<br>Pabilo St, Cebu City,<br>Cebu, 6000, Philippines</p>
    </div>
  </section>

  <!-- business card back -->
  <section class="sheet card card--back">
    <div class="card__frame"></div>
    <div class="brand" style="top:38px">
      <span class="brand__mark" style="width:17px;height:17px;margin-bottom:4px"></span>
      <span class="brand__name" style="font-size:10px">CORVINA TERRACE</span>
      <span class="brand__sub" style="font-size:6.5px">HOTEL</span>
    </div>
  </section>

  <!-- envelope -->
  <section class="sheet envelope">
    <div class="texture" role="img" aria-label="Soft silver speckle texture"></div>
    <div class="ghost-square" style="left:266px;top:53px;width:118px;height:168px;background:#e2e3e5"></div>
    <div class="brand" style="top:20px;left:20px;right:auto;width:170px">
      <span class="brand__mark" style="width:22px;height:22px"></span>
      <span class="brand__name" style="font-size:12px">CORVINA TERRACE</span>
      <span class="brand__sub" style="font-size:7.5px">HOTEL</span>
    </div>
    <p class="small envelope__contact">reservations@corvinaterracehotel.example<br>Magistrate Lunod Avenue corner<br>Pabilo St, Cebu City,<br>Cebu, 6000, Philippines</p>
    <div class="envelope__rule"></div>
  </section>

  <!-- letterhead -->
  <section class="sheet letterhead">
    <div class="texture" role="img" aria-label="Soft silver speckle texture"></div>
    <div class="brand" style="top:22px">
      <span class="brand__mark" style="width:22px;height:22px"></span>
      <span class="brand__name" style="font-size:12px">CORVINA TERRACE</span>
      <span class="brand__sub" style="font-size:7.5px">HOTEL</span>
    </div>
    <div class="ghost-square" style="left:100px;top:178px;width:156px;height:128px"></div>
    <div class="letterhead__foot small">
      <span class="line"></span>
      <p class="text">Magistrate Lunod Avenue corner Pabilo St, Cebu City, Cebu, 6000, Philippines<br>+63 32 481 7520 &nbsp;|&nbsp; +63 32 481 7534 &nbsp;|&nbsp; www.corvinaterracehotel.example</p>
      <span class="line"></span>
    </div>
  </section>

</body>
</html>
```